Hot-air ballooning company needs a DL-size flyer

Skylark Aerial Tours is a hot-air ballooning company which flies passengers in the King Valley, Victoria, Australia.
We need a 2-sided DL-size flyer which promotes our hot-air balloon flights and packages.
Most of our customers are couples, and we want the flyer design to communicate safety, adventure, and romance.
The flyer should make the best use of our images which we provide, and we've also included a document with the text for the flyer.
Updates

2 days is not long enough to gather designs, the brief never asked me what my deadline should be.

Target Market(s)

Couples, buyers are majority female, between the ages of 20-60

Industry/Entity Type

Tourism

Font styles to use
Sans Serif

Colors

Designer to choose colors to be used in the design.

Requirements
Must have
• Communicate safety, adventure, and romance
• Use images
Nice to have
• There is a lot of text, it would be great if you could make it look like as little text as possible
Should not have
• No childish designs

```html
<!DOCTYPE html>
<html lang="en">
<head>
<meta charset="utf-8">
<title>Skylark Aerial Tours – DL Flyer</title>
<link href="https://fonts.googleapis.com/css2?family=Oswald:wght@500;600&family=PT+Sans:ital,wght@0,400;0,700;1,400;1,700&family=Raleway:wght@300;400&family=Yellowtail&display=swap" rel="stylesheet">
<style>
  :root{
    --sky-deep:#0d6aab;
    --sky:#3a8fca;
    --sky-light:#7fb6dc;
    --navy:#1f3f66;
    --white:#ffffff;
    --gold:#f2c52e;
    --gold-band:#f7c934;
    --orange:#f0773a;
    --teal:#2f9eb0;
    --ink:#1c2430;
    --earth:#4a3d38;
  }
  *{box-sizing:border-box;margin:0;padding:0}
  html,body{width:1200px;height:1200px;overflow:hidden;background:#ffffff}
  body{position:relative;font-family:"PT Sans",sans-serif;color:var(--white)}
  .flyer{position:absolute;top:150px;width:451px;height:900px;overflow:hidden}
  .flyer--front{left:97px;background:linear-gradient(180deg,var(--sky-deep) 0%,var(--sky) 60%,var(--sky-light) 100%)}
  .flyer--back{left:653px;background:var(--sky)}
  .abs{position:absolute}

  /* Front */
  .front-title{top:34px;left:0;width:100%;text-align:center;font-family:"Oswald",sans-serif;font-weight:600;font-size:47px;line-height:50px;letter-spacing:-0.5px}
  .front-hero{top:120px;left:0;width:100%;height:271px;
    background:linear-gradient(180deg,rgba(58,143,202,0) 0%,#4f95c6 30%,#9fb8c8 55%,#c2ccd2 68%,#7b7c80 85%,var(--earth) 100%)}
  .front-tagline{top:330px;left:0;width:100%;text-align:center;font-family:"Raleway",sans-serif;font-weight:300;font-size:25px;line-height:22px}
  .front-intro{top:420px;left:34px;width:382px;font-style:italic;font-size:14.6px;line-height:18.5px;text-align:justify}
  .front-lower{top:545px;left:0;width:100%;height:355px;
    background:linear-gradient(180deg,rgba(127,182,220,0) 0%,#9cc1dd 35%,#bccbd6 58%,#8a8a8c 75%,#5a4a40 88%,#3e3631 100%)}
  .front-celebrate{top:586px;left:231px;width:185px;font-style:italic;font-size:16.5px;line-height:18.5px}
  .front-rule{top:653px;left:230px;width:182px;height:2px;background:var(--gold)}
  .front-milawa{top:665px;left:231px;width:185px;font-style:italic;font-size:15.5px;line-height:16px;color:var(--navy)}
  .front-mansfield{top:866px;left:0;width:100%;text-align:center;font-style:italic;font-weight:700;font-size:17px;color:var(--gold)}

  /* Back */
  .back-hero{top:0;left:0;width:100%;height:340px;
    background:linear-gradient(180deg,#c7dcec 0%,#e8d3a3 30%,#c98a3c 55%,#6f7d4a 75%,var(--sky) 100%)}
  .back-script{top:72px;left:30px;font-family:"Yellowtail",cursive;font-size:44px;color:#1766a9}
  .feature{left:43px;width:345px;font-style:italic;font-size:15.5px;line-height:18px}
  .feature-rule{left:43px;width:348px;height:2px;background:linear-gradient(90deg,var(--gold),rgba(242,197,46,0.3))}
  .ribbon{left:0;height:19px;background:var(--orange);clip-path:polygon(0 0,100% 0,calc(100% - 8px) 100%,0 100%);
    font-style:italic;font-size:14.5px;line-height:19px;padding-left:22px;white-space:nowrap}
  .ribbon::before{content:"•";margin-right:2px}
  .back-strip{top:690px;left:0;width:100%;height:62px;background:linear-gradient(180deg,#4d93c6 0%,#a9c1d3 55%,#8b9aa4 100%)}
  .booking-pill{top:738px;left:131px;width:190px;height:20px;border-radius:10px 10px 0 0;background:var(--teal);
    text-align:center;font-style:italic;font-weight:700;font-size:11.5px;line-height:20px}
  .contact-band{top:758px;left:0;width:100%;height:60px;background:var(--gold-band);color:var(--ink)}
  .contact-web{top:8px;left:28px;font-style:italic;font-weight:700;font-size:14px}
  .contact-mail{top:28px;left:24px;font-style:italic;font-size:14px;color:#333}
  .contact-call{top:7px;left:262px;font-style:italic;font-size:14.5px;color:#444}
  .contact-phone{top:20px;left:262px;font-family:"Oswald",sans-serif;font-weight:500;font-size:29px;letter-spacing:0.5px}
  .back-foot{top:818px;left:0;width:100%;height:82px;background:linear-gradient(180deg,#3a3a36,#2a2926)}
  .foot-find{top:4px;left:70px;font-style:italic;font-size:11px}
  .foot-icons{top:19px;left:52px;display:flex;gap:10px}
  .foot-icon{width:32px;height:32px;border-radius:5px;background:#6d7f96}
  .foot-handle{top:58px;left:20px;font-style:italic;font-size:14px}
  .foot-cert{top:25px;left:233px;font-size:11.2px;line-height:15px}
</style>
</head>
<body>

<section class="flyer flyer--front" aria-label="Flyer front">
  <h1 class="abs front-title">KING VALLEY<br>HOT-AIR BALLOONING</h1>
  <div class="abs front-hero" role="img" aria-label="Photo: colourful hot-air balloons over misty valley and winery at dawn"></div>
  <p class="abs front-tagline">The perfect gourmet<br>ballooning experience</p>
  <p class="abs front-intro">Live the romance and adventure of flying the beautiful King Valley and surrounds in a hot-air balloon at dawn. From the vineyards and patchwork of fields the views expand to the Ovens River, spectacular Mt Buffalo and the High Country beyond. The mountain views, once aloft, come to life in dramatic 3D with the early morning light</p>
  <div class="abs front-lower" role="img" aria-label="Photo: multicoloured hot-air balloon rising above a country estate and autumn trees"></div>
  <p class="abs front-celebrate">Celebrate your flight with a delicious breakfast afterwards (optional)</p>
  <div class="abs front-rule"></div>
  <p class="abs front-milawa">Milawa is conveniently located less than an hour's drive from most places in Victoria's North East<br>&amp; Albury in NSW</p>
  <p class="abs front-mansfield">Mansfield flights are also available</p>
</section>

<section class="flyer flyer--back" aria-label="Flyer back">
  <div class="abs back-hero" role="img" aria-label="Photo: passengers in a balloon basket above a river at sunrise"></div>
  <p class="abs back-script">Your flight</p>

  <p class="abs feature" style="top:285px">One-hour sunrise balloon flight in the spectacular King Valley region in North East Victoria</p>
  <div class="abs feature-rule" style="top:328px"></div>
  <p class="abs feature" style="top:340px">Delicious champagne breakfast after the flight (recommended option)</p>
  <div class="abs feature-rule" style="top:383px"></div>
  <p class="abs feature" style="top:395px">Informative details throughout your experience with our locally based expert crew</p>
  <div class="abs feature-rule" style="top:438px"></div>
  <p class="abs feature" style="top:450px">The opportunity to be involved in the inflation and deflation process should you wish</p>

  <p class="abs ribbon" style="top:503px;width:238px">Safe, friendly and professional</p>
  <p class="abs ribbon" style="top:530px;width:279px">The flight lasts approximately 1 hour</p>
  <p class="abs ribbon" style="top:557px;width:323px">The entire experience takes about 3-4 hours</p>
  <p class="abs ribbon" style="top:585px;width:206px">Suitable from age 7 to 97</p>
  <p class="abs ribbon" style="top:612px;width:243px">Gift Vouchers are also available</p>
  <p class="abs ribbon" style="top:640px;width:441px">Contact us for exclusive flight options at your custom location</p>

  <div class="abs back-strip" role="img" aria-label="Photo: many balloons drifting over a misty plain"></div>
  <p class="abs booking-pill">For bookings or more information</p>

  <div class="abs contact-band">
    <p class="abs contact-web">www.skylarkaerialtours.com.au</p>
    <p class="abs contact-mail">flights@skylarkaerialtours.com.au</p>
    <p class="abs contact-call">or call our friendly team on</p>
    <p class="abs contact-phone">1300 759 275</p>
  </div>

  <div class="abs back-foot">
    <p class="abs foot-find">Find us also on</p>
    <div class="abs foot-icons" aria-hidden="true">
      <span class="foot-icon"></span><span class="foot-icon"></span><span class="foot-icon"></span>
    </div>
    <p class="abs foot-handle">@skylarkaerialtours</p>
    <p class="abs foot-cert">Skylark Aerial Tours operates under<br>Air Operator's Certificate <b>C481337-05</b><br>issued by the National Air Safety Authority</p>
  </div>
</section>

</body>
</html>
```